Business Cards - Flexible and open for new ideas!

Ledger Bloom is a service designed to assist both businesses and individuals in managing their paper receipts. We do this by scanning paper receipts and storing them as pdf files which are downloadable to access and view at any time. We extract the data from each receipt so it can also be downloaded in the form for TallyWorks, Fiscora, Excel, KPLT or CSV. There is no need to manually do this anymore. Our site also offers various reporting and graphing functionalities to track and manage expenditures. Our goal is to take the stress and disorganization out of tax time and help businesses to receive as much deduction on their expenses over the year as possible.

I have created a logo which I like but comments and alternate logos are encouraged. I have included my PSD and Font file with the project. If you cant download them I can send them to you. Alternatively our current styling is viewable on our website at ledgerbloomhub.com.au.

(We are still open to new designs and colours and are happy to modify our logo/website etc. if you can recommend something better!)
Updates

Rosalind has cleared up the hexagon stack and we really like that if you could do this that would be great!. 

Warm regards,

Ledger Bloom

On the back of the card we are really liking the large hexagon stack with no words either in the background or white overlaying the background. With the logo and the information to the side.

Due to the great responses we have now guaranteed the project!

The front of the card should have:

- Cleaned up hexagon stack with even spaces between the hexagons.
- Text same size and next to hexagon stack like in the logo
- The website on the front of the card
- The background to contain multiple hexagon stacks 

Back of the card:

- Contain the logo
- Use the hexagon stack as a background for part of the card (1/4 or 1/2)
- Space for address and 2 telephone numbers

Thanks for all that have posted designs so far!

Even thought we have the above current ideas, we are still open for any left field design. We can only comment on the above designs because we have seen them. If you have an idea or can create something that you think is great please feel free to submit it! 

Hey all.

We have had some fantastic designs and really would enjoy any final designs before the deadline this weekend.

If you have a totally unique idea please feel free to submit it even if you have already submitted something else.

If you feel you are unsure of what we want or we havent provided enough feedback please contact us and we can sort it out.

Target Market(s)

We are aiming for small to medium business owners, accountants and bookkeepers

Industry/Entity Type

Business

Requirements
Must have
• We would like to include our logo, which is navy blue for the hexagon stack and black for the title. Colours should include dark navy blues, lighters blues, black for other designs on the card.

We would like our web address, phone number and mailing address present; preferably be on the back of the business card, but feel free to wow us if you think you have a design but doesn't necessarily fit our guidelines :)
Should not have
• Dont like too much happening. Prefer simple and bold.

```html
<!DOCTYPE html>
<html lang="en">
<head>
<meta charset="utf-8">
<title>Ledger Bloom – Business Cards</title>
<link rel="stylesheet" href="https://fonts.googleapis.com/css2?family=Archivo:wght@800&family=Noto+Sans:wght@400&family=Noto+Serif:wght@700&display=swap">
<style>
  :root {
    --page-bg: #e6e6e8;
    --blue-light: #2f93e6;
    --blue-mid: #1b74cf;
    --blue-deep: #0b4ea6;
    --navy: #2a2a86;
    --ink: #141414;
    --white: #ffffff;
    --silver-light: #f4f4f6;
    --silver-dark: #bfc0c6;
    --hex-tint: #c9c8e2;
  }
  * { margin: 0; padding: 0; box-sizing: border-box; }
  html, body {
    width: 1200px;
    height: 951px;
    overflow: hidden;
    background: var(--page-bg);
  }
  .stage { position: relative; width: 1200px; height: 951px; }

  .card {
    position: absolute;
    overflow: hidden;
    box-shadow: 0 10px 24px rgba(0,0,0,0.28);
  }

  /* Front card */
  .card-front {
    left: 40px; top: 70px;
    width: 660px; height: 380px;
    background: radial-gradient(ellipse at 50% 45%, var(--blue-light) 0%, var(--blue-mid) 50%, var(--blue-deep) 100%);
  }
  .front-pattern {
    position: absolute; inset: 0;
    background: radial-gradient(ellipse at 20% 20%, rgba(255,255,255,0.12), transparent 45%),
                radial-gradient(ellipse at 85% 80%, rgba(255,255,255,0.10), transparent 45%);
  }
  .front-brand {
    position: absolute;
    left: 130px; top: 128px;
    display: flex; align-items: center; gap: 22px;
  }
  .brand-dot {
    width: 58px; height: 58px;
    border-radius: 50%;
    background: var(--navy);
  }
  .brand-name {
    font-family: "Archivo", sans-serif;
    font-weight: 800;
    color: var(--ink);
    letter-spacing: -1px;
    line-height: 1;
  }
  .front-brand .brand-name { font-size: 66px; }
  .front-web {
    position: absolute;
    left: 0; right: 0; bottom: 44px;
    text-align: center;
    font-family: "Archivo", sans-serif;
    font-weight: 800;
    font-size: 22px;
    color: var(--white);
    letter-spacing: 0.5px;
  }

  /* Back card */
  .card-back {
    left: 400px; top: 480px;
    width: 740px; height: 420px;
    background: linear-gradient(135deg, var(--silver-light) 0%, #dcdce2 55%, var(--silver-dark) 100%);
  }
  .back-pattern {
    position: absolute;
    right: 0; top: 0;
    width: 360px; height: 100%;
    background: radial-gradient(ellipse at 55% 45%, rgba(201,200,226,0.55), rgba(201,200,226,0.15) 70%);
  }
  .back-panel {
    position: absolute;
    left: 0; top: 0;
    width: 420px; height: 100%;
  }
  .contact {
    position: absolute;
    left: 50px; top: 56px;
    color: var(--white);
  }
  .contact-name {
    font-family: "Noto Serif", serif;
    font-weight: 700;
    font-size: 25px;
  }
  .contact-role {
    font-family: "Noto Sans", sans-serif;
    font-size: 16px;
    margin-top: 2px;
  }
  .contact-list {
    list-style: none;
    margin-top: 52px;
    font-family: "Noto Sans", sans-serif;
    font-size: 17px;
    line-height: 24px;
  }
  .contact-list li { display: flex; align-items: flex-start; gap: 12px; }
  .contact-list .icon { width: 16px; height: 16px; margin-top: 4px; flex: none; }
  .contact-list .gap { height: 12px; }
  .back-brand {
    position: absolute;
    left: 470px; top: 186px;
    display: flex; align-items: center; gap: 16px;
  }
  .back-brand .brand-dot { width: 44px; height: 44px; }
  .back-brand .brand-name { font-size: 42px; }
</style>
</head>
<body>
<main class="stage">

  <section class="card card-front" aria-label="Business card front">
    <div class="front-pattern" role="img" aria-label="Background of repeated hexagon stacks in light blue"></div>
    <div class="front-brand">
      <span class="brand-dot"></span>
      <span class="brand-name">Ledger Bloom</span>
    </div>
    <p class="front-web">www.ledgerbloomhub.com.au</p>
  </section>

  <section class="card card-back" aria-label="Business card back">
    <div class="back-pattern" role="img" aria-label="Large faint hexagon stack pattern"></div>
    <svg class="back-panel" viewBox="0 0 420 420" preserveAspectRatio="none" aria-hidden="true">
      <defs>
        <linearGradient id="panelBlue" x1="0" y1="0" x2="1" y2="1">
          <stop offset="0" stop-color="#2b8de2"/>
          <stop offset="1" stop-color="#0f5bb5"/>
        </linearGradient>
      </defs>
      <path d="M0 0 H400 Q370 210 400 420 H0 Z" fill="#ffffff"/>
      <path d="M0 0 H392 Q362 210 392 420 H0 Z" fill="url(#panelBlue)"/>
    </svg>

    <div class="contact">
      <p class="contact-name">Martin Kell</p>
      <p class="contact-role">director</p>
      <ul class="contact-list">
        <li>
          <svg class="icon" viewBox="0 0 16 16" aria-hidden="true"><path d="M8 1 L15 8 H13 V15 H3 V8 H1 Z" fill="#fff"/></svg>
          <span>P.O. Box 246810<br>Harlow Bay, WI 50317</span>
        </li>
        <li class="gap"></li>
        <li>
          <svg class="icon" viewBox="0 0 16 16" aria-hidden="true"><path d="M4 1 L6.5 4 L5 6 Q6.5 9.5 10 11 L12 9.5 L15 12 L13 15 Q3 13 1 3 Z" fill="#fff"/></svg>
          <span>888-310-4472</span>
        </li>
        <li>
          <svg class="icon" viewBox="0 0 16 16" aria-hidden="true"><rect x="2" y="1" width="12" height="14" rx="2" fill="#fff"/><rect x="4" y="3" width="8" height="6" fill="#1b74cf"/></svg>
          <span>888-629-0815</span>
        </li>
        <li>
          <svg class="icon" viewBox="0 0 16 16" aria-hidden="true"><circle cx="8" cy="8" r="7" fill="#fff"/></svg>
          <span>www.ledgerbloomhub.com.au</span>
        </li>
        <li>
          <svg class="icon" viewBox="0 0 16 16" aria-hidden="true"><rect x="1" y="3" width="14" height="10" rx="1" fill="#fff"/><path d="M1 4 L8 9 L15 4" stroke="#1b74cf" stroke-width="1.5" fill="none"/></svg>
          <span>info@ledgerbloomhub.com.au</span>
        </li>
      </ul>
    </div>

    <div class="back-brand">
      <span class="brand-dot"></span>
      <span class="brand-name">Ledger Bloom</span>
    </div>
  </section>

</main>
</body>
</html>
```